Climbing Gear Company Stationary Design

We need some new stationary to standardise our business.
We require:

Business Card
A4 Letterhead
With complements slip

Our business is a Distributor and retailer of rock climbing equipment throughout Australia.
We need to the stationary (business card in particular) to reflect this.

Target Market(s)

customers, other retail outlets, overseas manufacturers.

Industry/Entity Type

Business

Requirements
Must have
• company logo
website url- www.crestwardsupply.com.au
email - marlo@crestwardsupply.com
Business Address: Unit 3, 14-16 Quarry Close, Port Bellamy, NSW, 2471
Phone: 0491 637 208
my Name (on Business card) - Marlon Pettigrew
use of Blue colour in our logo

```html
<!DOCTYPE html>
<html lang="en">
<head>
<meta charset="utf-8">
<title>Crestward Supply Stationery</title>
<link rel="stylesheet" href="https://fonts.googleapis.com/css2?family=Arimo:wght@400;700&display=swap">
<style>
  :root {
    --brand-blue: #2b3990;
    --ink: #3a3a3a;
    --muted: #8a8a8a;
    --paper: #f6f6f6;
    --deco-light: #ececec;
    --deco-dark: #dadada;
    --label-grey: #d0d0d0;
    --canvas: #ffffff;
  }
  * { box-sizing: border-box; margin: 0; padding: 0; }
  html, body { width: 1200px; height: 1200px; overflow: hidden; background: var(--canvas); }
  body { position: relative; font-family: "Arimo", Arial, sans-serif; color: var(--ink); }

  .wordmark { position: absolute; color: var(--brand-blue); font-weight: 700; letter-spacing: 0.02em; white-space: nowrap; line-height: 1; }
  .tagline { position: absolute; color: var(--brand-blue); font-weight: 400; letter-spacing: 0.16em; white-space: nowrap; line-height: 1; }

  .presentation-mark .wordmark { left: 724px; top: 51px; font-size: 29px; }
  .presentation-mark .tagline { left: 725px; top: 86px; font-size: 10.5px; }
  .option-number { position: absolute; left: 842px; top: 163px; font-size: 30px; color: var(--label-grey); font-weight: 400; }

  .sheet { position: absolute; background: var(--paper); box-shadow: 0 1px 3px rgba(0,0,0,0.18); overflow: hidden; }

  .deco-climber { position: absolute; background: radial-gradient(ellipse at 55% 45%, var(--deco-dark) 0%, var(--deco-light) 50%, rgba(236,236,236,0) 75%); }
  .deco-strip { position: absolute; top: 0; bottom: 0; background: linear-gradient(180deg, var(--deco-light), var(--paper)); }

  /* Letterhead */
  .letterhead { left: 93px; top: 322px; width: 580px; height: 744px; }
  .letterhead .deco-strip { right: 0; width: 24px; }
  .letterhead .deco-climber { left: 470px; top: 50px; width: 110px; height: 150px; }
  .letterhead .wordmark { left: 68px; top: 41px; font-size: 21px; }
  .letterhead .tagline { left: 69px; top: 66px; font-size: 7.6px; }
  .sender-details { position: absolute; left: 68px; top: 92px; font-size: 7.4px; line-height: 10.5px; color: var(--muted); }
  .letter-body { position: absolute; left: 68px; top: 192px; width: 420px; font-size: 8.6px; line-height: 13.6px; color: var(--ink); }
  .letter-body p { margin-bottom: 13.6px; }
  .letter-body .salutation { margin-bottom: 27px; }
  .letter-body .closing { margin-top: 14px; margin-bottom: 4px; }
  .signature { display: block; width: 140px; height: 40px; margin: 0 0 4px; background: linear-gradient(90deg, rgba(43,57,144,0.08), rgba(43,57,144,0.01)); }
  .signoff { line-height: 12px; }

  /* Business card */
  .card-back { left: 838px; top: 600px; width: 125px; height: 200px; transform: rotate(8deg); transform-origin: top left; background: #e2e2e2; }
  .card-back .deco-climber { left: 30px; top: 55px; width: 80px; height: 110px; }
  .card-back .deco-strip { right: 0; width: 16px; background: linear-gradient(180deg, #d6d6d6, #e6e6e6); }
  .card-front { left: 779px; top: 534px; width: 128px; height: 205px; background: #fafafa; }
  .card-front .wordmark { left: 17px; top: 27px; font-size: 8.6px; }
  .card-front .tagline { left: 17px; top: 38px; font-size: 3.4px; letter-spacing: 0.1em; }
  .card-name { position: absolute; left: 17px; top: 100px; font-size: 8.5px; line-height: 10px; font-weight: 700; color: var(--brand-blue); }
  .card-title { position: absolute; left: 17px; top: 123px; font-size: 4.5px; color: var(--muted); }
  .card-details { position: absolute; left: 17px; top: 143px; font-size: 4.6px; line-height: 6.5px; color: var(--muted); }

  /* Compliments slip */
  .comp-slip { left: 617px; top: 784px; width: 511px; height: 253px; }
  .comp-slip .deco-strip { right: 0; width: 20px; }
  .comp-slip .deco-climber { left: 400px; top: 40px; width: 105px; height: 125px; }
  .comp-slip .wordmark { left: 27px; top: 28px; font-size: 19px; }
  .comp-slip .tagline { left: 28px; top: 51px; font-size: 7.2px; }
  .slip-footer { position: absolute; left: 27px; top: 229px; font-size: 6.2px; color: var(--muted); white-space: nowrap; }
  .slip-footer strong { color: var(--ink); }
</style>
</head>
<body>

  <header class="presentation-mark">
    <div class="wordmark">CRESTWARD SUPPLY</div>
    <div class="tagline">THE ROPE•THE ROUTE•THE SUMMIT</div>
  </header>
  <div class="option-number">#1</div>

  <article class="sheet letterhead">
    <div class="deco-strip"></div>
    <div class="deco-climber" role="img" aria-label="Faint climber silhouette on a rock wall"></div>
    <div class="wordmark">CRESTWARD SUPPLY</div>
    <div class="tagline">THE ROPE•THE ROUTE•THE SUMMIT</div>
    <div class="sender-details">
      Unit 3, 14-16 Quarry Close, Port Bellamy, NSW, 2471<br>
      Phone: 0491 637 208 • www.crestwardsupply.com.au
    </div>
    <div class="letter-body">
      <p class="salutation">Dear Sir,</p>
      <p>Thank you for your recent enquiry about our climbing range. Your order has been received and is being prepared for dispatch from our warehouse. Our team has checked each item against your list, including ropes, harnesses, carabiners and belay devices, and everything is in stock. Delivery should arrive within five working days, and tracking details will follow by email shortly.</p>
      <p>We have also included our latest trade catalogue, which features new season gear from our overseas partners. Retail outlets ordering in bulk receive tiered pricing and priority freight across Australia. Please contact us if you would like samples or a demonstration.</p>
      <p>We look forward to working with you again. Should you have any questions about fitting, care or warranty, our staff are always happy to help by phone or email.</p>
      <p class="closing">Best regards,</p>
      <span class="signature" role="img" aria-label="Handwritten signature"></span>
      <div class="signoff">Marlon Pettigrew<br>title</div>
    </div>
  </article>

  <section class="sheet card-back">
    <div class="deco-strip"></div>
    <div class="deco-climber" role="img" aria-label="Climber silhouette on a rock wall"></div>
  </section>

  <section class="sheet card-front">
    <div class="wordmark">CRESTWARD SUPPLY</div>
    <div class="tagline">THE ROPE•THE ROUTE•THE SUMMIT</div>
    <div class="card-name">Marlon<br>Pettigrew</div>
    <div class="card-title">title</div>
    <div class="card-details">
      Crestward Supply<br>
      Unit 3, 14-16 Quarry Close<br>
      Port Bellamy NSW 2471<br>
      Phone: 0491 637 208<br>
      www.crestwardsupply.com.au
    </div>
  </section>

  <section class="sheet comp-slip">
    <div class="deco-strip"></div>
    <div class="deco-climber" role="img" aria-label="Faint climber silhouette on a rock wall"></div>
    <div class="wordmark">CRESTWARD SUPPLY</div>
    <div class="tagline">THE ROPE•THE ROUTE•THE SUMMIT</div>
    <div class="slip-footer"><strong>Crestward Supply</strong> • Unit 3, 14-16 Quarry Close, Port Bellamy, NSW, 2471 • Phone: 0491 637 208 • www.crestwardsupply.com.au</div>
  </section>

</body>
</html>
```